Tovimerra: Travel business card redesign

We need a clean elegant look for our cards featuring blue and orange. Look should communicate a sense of strong design and seem uncluttered. The company is Tovimerra which means sail into calm. As in every trip is an sail into calm. Feel free to reinvent the logo or just tweak it. Colors should be blue like Caribbean waters and a saturated orange. Keep it clean and simple.
Please match the information in the sample uploaded but the sample is horrible -- a non-starter -- use for information only. also please add managing director to my name as title

Target Market(s)
potential clients, hotels, trade publications
Industry/Entity Type
Travel Industry
Contact Information for Business Card
as above
Requirements
Must have
- Font should be century gothic. Colors below are close but a but prefer lighter in each case.

```html
<!DOCTYPE html>
<html lang="en">
<head>
<meta charset="utf-8">
<title>Tovimerra business card</title>
<link rel="stylesheet" href="https://fonts.googleapis.com/css2?family=Mulish:wght@400;600;800&display=swap">
<style>
  :root{
    --backdrop:#2a2a2c;
    --card:#121212;
    --orange:#f7862c;
    --blue:#2196e0;
    --ink:#111111;
  }
  *{box-sizing:border-box;margin:0;padding:0}
  html,body{width:1200px;height:900px;overflow:hidden}
  body{background:var(--backdrop);font-family:"Mulish",sans-serif;position:relative}
  .card{position:absolute;top:118px;width:380px;height:665px;background:var(--card);
        box-shadow:0 14px 34px rgba(0,0,0,.55)}
  .card--front{left:175px}
  .card--back{left:645px}

  .holder{position:absolute;top:52px;right:40px;text-align:right}
  .holder__name{color:var(--orange);font-size:23px;font-weight:600;letter-spacing:.3px}
  .holder__title{color:var(--blue);font-size:13px;font-weight:600;margin-top:2px}

  .brand{position:absolute;left:0;right:0;text-align:center}
  .card--front .brand{top:270px}
  .card--back .brand{top:230px}
  .brand__name{color:var(--orange);font-size:58px;font-weight:800;letter-spacing:-1px;line-height:1}
  .brand__tagline{color:var(--blue);font-size:22px;font-weight:400;letter-spacing:1px;margin-top:8px;
                  text-align:right;padding-right:44px}

  .contacts{position:absolute;left:0;top:505px;list-style:none}
  .contact{display:flex;align-items:center;height:34px}
  .contact__stripe{width:66px;height:16px;background:var(--blue)}
  .contact__icon{width:28px;height:28px;background:var(--orange);margin-left:4px;
                 display:flex;align-items:center;justify-content:center}
  .contact__icon svg{width:18px;height:18px}
  .contact__text{color:var(--blue);font-size:16px;font-weight:600;margin-left:12px;line-height:1.15;white-space:nowrap}
  .contact--address{height:48px}

  .service-band{position:absolute;left:0;bottom:84px;width:380px;height:40px}
  .service-band__text{font-family:"Mulish",sans-serif;font-size:15px;font-weight:600;fill:var(--ink)}
</style>
</head>
<body>

<section class="card card--front" aria-label="Card front">
  <div class="holder">
    <p class="holder__name">Leo Varnell</p>
    <p class="holder__title">Managing Director</p>
  </div>

  <div class="brand">
    <p class="brand__name">tovimerra</p>
    <p class="brand__tagline">sail into calm</p>
  </div>

  <ul class="contacts">
    <li class="contact">
      <span class="contact__stripe"></span>
      <span class="contact__icon">
        <svg viewBox="0 0 24 24" aria-hidden="true"><path fill="#111" d="M6.6 10.8a15.1 15.1 0 0 0 6.6 6.6l2.2-2.2a1 1 0 0 1 1-.25 11.4 11.4 0 0 0 3.6.57 1 1 0 0 1 1 1V20a1 1 0 0 1-1 1A17 17 0 0 1 3 4a1 1 0 0 1 1-1h3.5a1 1 0 0 1 1 1 11.4 11.4 0 0 0 .57 3.6 1 1 0 0 1-.25 1z"/></svg>
      </span>
      <span class="contact__text">877.86.TOVI (868400)</span>
    </li>
    <li class="contact">
      <span class="contact__stripe"></span>
      <span class="contact__icon">
        <svg viewBox="0 0 24 24" aria-hidden="true"><rect x="5" y="2" width="14" height="20" rx="2" fill="#111"/><rect x="7.5" y="4.5" width="9" height="4" fill="#f7862c"/><g fill="#f7862c"><rect x="7.5" y="11" width="2.5" height="2.5"/><rect x="11" y="11" width="2.5" height="2.5"/><rect x="14.5" y="11" width="2.5" height="2.5"/><rect x="7.5" y="15" width="2.5" height="2.5"/><rect x="11" y="15" width="2.5" height="2.5"/><rect x="14.5" y="15" width="2.5" height="2.5"/></g></svg>
      </span>
      <span class="contact__text">323.555.0142</span>
    </li>
    <li class="contact">
      <span class="contact__stripe"></span>
      <span class="contact__icon">
        <svg viewBox="0 0 24 24" aria-hidden="true"><rect x="7" y="3" width="10" height="5" fill="#111"/><rect x="3" y="8" width="18" height="9" rx="1.5" fill="#111"/><rect x="7" y="14" width="10" height="7" fill="#111" stroke="#f7862c" stroke-width="1.2"/></svg>
      </span>
      <span class="contact__text">310.555.0187</span>
    </li>
    <li class="contact contact--address">
      <span class="contact__stripe"></span>
      <span class="contact__icon">
        <svg viewBox="0 0 24 24" aria-hidden="true"><path fill="#111" d="M12 3 2 12h3v9h5v-6h4v6h5v-9h3z"/></svg>
      </span>
      <span class="contact__text">1460 Harbor Crest Way N,<br>Bayview Hills, 90812</span>
    </li>
  </ul>
</section>

<section class="card card--back" aria-label="Card back">
  <div class="brand">
    <p class="brand__name">tovimerra</p>
    <p class="brand__tagline">sail into calm</p>
  </div>

  <svg class="service-band" viewBox="0 0 380 40" role="group" aria-label="Service line">
    <polygon points="0,25 78,25 74,35 0,35" fill="var(--blue)"/>
    <polygon points="70,36 82,8 322,8 310,36" fill="var(--orange)"/>
    <polygon points="318,9 380,9 380,19 314,19" fill="var(--blue)"/>
    <text class="service-band__text" x="196" y="27" text-anchor="middle">a first in service company</text>
  </svg>
</section>

</body>
</html>
```